Corvelle Matchmaking - Innovative AI-based Online Dating App

Hello, I am creating a new online dating app that subsumes the personalization and compatibility analysis of human matchmaking, but is combined with the convenience of modern dating apps such as brisket. The app is called Corvelle.

There is a lot of pain and fatigue in modern online dating. Corvelle uses a concise but effective questionnaire that is combined with cutting-edge AI, social psychology research, and psycholinguistic modelling to effectively and conveniently find dating matches with real compatibility - as opposed to any major app on the market. A personalized introduction for every user is generated everyday to introduce you to a new potential match - this introduction is totally unique and will never be seen before or again. The introduction is intertwined with the user’s images to create an attractive “newsletter” feel.

"Corvelle" is Italian for lagoon, which is "a shallow body of water protected from a larger body of water (usually the ocean) by sandbars, barrier islands, or coral reefs." Lagoons are beautiful, tropical, lush watery paradises - as I see it. This is meant to be the inspiration for the feel, color scheme and design of the app.

To that end, I have included concept images of lagoons to evoke the feeling of a paradise getaway where one may meet their soulmate. This is the feeling I would like to convey with the minimalist app design this product needs to compete.

I have included screenshots of the current app UI. There is a screen for
1) potential matches and incoming likes (just like Brisket) with a logo at the top. There are “Like”, “Dislike”, “Super Like”, and “Super Dislike” buttons that float over the screen as it scrolls. These button shape/colors likely need to change to match the rest of the design
2) Overview of message threads with each match
3) View of message threads
4) Settings page

I would like
1) the logo/header image to be redone (as well as the like/dislike/super like/super dislike buttons to be redone to match the new design)
2) icons for the 4 pages in the bottom navigation bar to be redone
3) color scheme to be optimized and evoking of the desired paradise but professional feeling of a hyper-intelligent (but also empathetic) matchmaker
4) design for the settings screen (to look professional and competitive with other dating apps)

The color scheme /layout/spacing/font(s) for the bubbles on the screen where new potential matches are introduced is the most important part of the design I’m looking for. It’s currently a stack of rounded rectangles basically, but I’m open to all ideas to make this app look as professional as possible while conveying the desired elegance, empathy, and uniqueness of the brand.

Thank you!

Target Market(s)

Single men and women ages 20 - 45

Industry/Entity Type

Online dating / Matchmaking

Requirements
Must have
• For the main screen where new users are being introduced (i.e. the "swipe" page on most dating apps) - some amount of matchmaking introductory text MUST be shown above the user's first profile picture, as indicated in the current screenshots.
Nice to have
• Re-designs of the top "Corvelle" logo/emblem would be nice. If changing the logo, some emblem or graphic in addition to just the text of "Corvelle" would be nice. (Like the way "plumway" has its red flame emblem)
Should not have
• The main "swipe" page should not look identical to other dating apps in the sense of being >90% just a user's first dating profile image. The competitive edge to this app is the user-to-user specific matchmaking introductory text, so some of that must be visible before a user scrolls down for further profile information.

```html
<!DOCTYPE html>
<html lang="en">
<head>
<meta charset="utf-8">
<title>Corvelle — App Design Board</title>
<link href="https://fonts.googleapis.com/css2?family=Poppins:wght@400;500;600;700&display=swap" rel="stylesheet">
<style>
:root{
  --green:#34c26a;
  --teal:#2aa596;
  --blue:#1a5ce0;
  --deep-blue:#0f46d6;
  --ink:#14161c;
  --muted:#8a8f98;
  --soft:#f2f3f5;
  --pink:#e8307a;
  --frame:#0b0e17;
  --white:#ffffff;
}
*{margin:0;padding:0;box-sizing:border-box}
html,body{width:1200px;height:2590px;overflow:hidden}
body{font-family:'Poppins',sans-serif;color:var(--ink);background:linear-gradient(135deg,var(--green) 0%,var(--teal) 45%,var(--blue) 100%);position:relative}
.board{position:absolute;left:15px;top:15px;width:1170px;height:2560px;background:var(--white);border-radius:22px}
.abs{position:absolute}
.defs{position:absolute;width:0;height:0;overflow:hidden}

/* brand */
.brand{position:absolute;left:150px;top:96px;display:flex;align-items:center;gap:14px}
.brand-name{font-size:58px;font-weight:500;letter-spacing:6px;color:var(--teal);line-height:1}
.brand-dot{width:16px;height:16px;border-radius:50%;background:var(--blue)}

/* tags */
.tag{position:absolute;height:44px;padding:0 16px;border-radius:9px;font-size:16px;font-weight:600;display:flex;align-items:center;
  border:2px solid transparent;background:linear-gradient(#fff,#fff) padding-box,linear-gradient(90deg,var(--green),var(--blue)) border-box}

/* vertical labels */
.label{position:absolute;writing-mode:vertical-rl;transform:rotate(180deg);font-size:12px;font-weight:700;letter-spacing:11px;color:var(--teal)}

/* screens */
.screen{position:absolute;width:280px;border:5px solid var(--frame);border-radius:32px;overflow:hidden;background:var(--white)}
.hero{transform-origin:0 0}
.status{position:absolute;left:0;top:0;width:100%;height:30px;z-index:5;display:flex;justify-content:space-between;align-items:center;padding:0 22px 0 24px;font-size:11px;font-weight:600;color:var(--white)}
.status svg{width:42px;height:10px}
.home-bar{position:absolute;left:50%;width:96px;height:4px;margin-left:-48px;border-radius:3px;background:var(--ink);z-index:6}
.home-bar.light{background:var(--white)}
.wordmark{position:absolute;left:0;width:100%;text-align:center;font-weight:500;letter-spacing:3px;color:var(--white);z-index:4}

/* splash */
.lagoon{position:absolute;inset:0;background:linear-gradient(180deg,#43a89f 0%,#3a9fa4 30%,#2b8fb0 60%,#1f6fc2 100%)}
.btn{position:absolute;height:36px;border-radius:18px;font-size:12px;font-weight:600;display:flex;align-items:center;justify-content:center}
.btn-outline{border:1.5px solid var(--white);color:var(--white)}
.btn-solid{background:var(--white);color:var(--teal)}

/* sign in */
.signin-card{position:absolute;left:0;top:177px;width:100%;bottom:0;background:var(--white);border-radius:18px 18px 0 0}
.signin-title{position:absolute;left:22px;top:118px;font-size:16px;font-weight:600}
.field{position:absolute;left:22px;width:226px;height:34px;border-radius:6px;background:var(--soft);display:flex;align-items:center;gap:10px;padding-left:12px;font-size:9px;color:#a6abb3}
.field svg{width:11px;height:11px}
.forgot{position:absolute;left:0;width:100%;text-align:center;top:243px;font-size:10px;font-weight:600;color:var(--blue)}
.login{position:absolute;left:22px;top:277px;width:226px;height:35px;border-radius:18px;background:linear-gradient(90deg,var(--green),var(--blue));color:var(--white);font-size:11px;font-weight:600;display:flex;align-items:center;justify-content:center}
.signup-line{position:absolute;left:0;width:100%;top:362px;text-align:center;font-size:8.5px;color:#555}
.signup-line b{color:var(--blue);font-weight:700;margin-left:6px}

/* discover */
.hdr{position:absolute;left:0;top:0;width:100%;z-index:2}
.disc-title{position:absolute;left:14px;font-size:18px;font-weight:600}
.greet{position:absolute;left:14px;font-size:8.5px;color:#333}
.copy{position:absolute;left:14px;width:244px;font-size:8.5px;line-height:16px;color:#333}
.copy .name{color:var(--blue)}
.photo{position:absolute;border-radius:12px;background:radial-gradient(circle at 55% 35%,#2b3f8a 0%,#16225c 55%,#0c1440 100%)}
.photo.beach{background:linear-gradient(180deg,#b8cfe0 0%,#d9c9ae 60%,#c7b08c 100%)}
.photo.sky{background:linear-gradient(180deg,#a7cde8 0%,#e6eef3 60%,#cdb994 100%)}
.actions{position:absolute;left:0;width:100%;display:flex;justify-content:center;align-items:center;gap:10px;z-index:4}
.act{border-radius:50%;background:var(--white);box-shadow:0 3px 10px rgba(20,30,60,.18);display:flex;align-items:center;justify-content:center}
.act.sm{width:32px;height:32px}
.act.lg{width:44px;height:44px}
.act svg{width:52%;height:52%}
.nav{position:absolute;left:0;width:100%;z-index:3}
.nav-icons{position:absolute;left:0;width:100%;display:flex;justify-content:space-around;padding:0 22px;z-index:4}
.nav-icons svg{width:17px;height:17px}

/* profile */
.prof-card{position:absolute;left:14px;width:242px;background:var(--white);border-radius:10px;box-shadow:0 2px 10px rgba(20,30,60,.1);padding:10px 12px}
.prof-name{font-size:17px;font-weight:600;display:flex;align-items:center;gap:6px}
.prof-name i{width:7px;height:7px;border-radius:50%;background:var(--green);display:block}
.prof-role{font-size:8.5px;color:var(--muted);margin-top:2px;display:flex;justify-content:space-between}
.chips{display:flex;flex-wrap:wrap;gap:5px 6px;margin-top:10px}
.chip{background:linear-gradient(90deg,#2f7fe0,var(--blue));color:var(--white);font-size:7px;padding:3px 10px;border-radius:9px}
.sign{position:absolute;left:14px;display:flex;align-items:center;gap:8px;font-size:8.5px;font-weight:500}
.avatar{border-radius:50%;background:linear-gradient(135deg,#8fa6c4,#3c5a8a)}
.more{position:absolute;left:14px;width:242px;height:272px;border-radius:10px;background:var(--white);box-shadow:0 2px 12px rgba(20,30,60,.1);padding:16px 14px}
.more h4{font-size:10.5px;font-weight:600}
.facts{margin-top:14px;height:48px;border-radius:6px;background:var(--soft);display:flex;justify-content:space-around;align-items:center}
.fact{text-align:center}
.fact small{display:block;font-size:6px;color:var(--muted);letter-spacing:.5px}
.fact span{font-size:8.5px;font-weight:500;display:flex;align-items:center;gap:6px;margin-top:2px}
.fact svg{width:11px;height:11px}
.row{display:flex;justify-content:space-between;align-items:center;height:33px;border-bottom:1px dashed #e2e4e8;font-size:8.5px}
.row:last-child{border-bottom:none}
.row small{font-size:7px;color:var(--muted);letter-spacing:.5px}
.row span{font-weight:500}
.thread-name{position:absolute;left:0;width:100%;top:30px;text-align:center;color:var(--white);font-size:9.5px;font-weight:500;z-index:4}
</style>
</head>
<body>

<svg class="defs" aria-hidden="true">
  <defs>
    <linearGradient id="g-header" x1="0" y1="0" x2="1" y2="0">
      <stop offset="0" stop-color="#2ba48f"/><stop offset="1" stop-color="#1a5fd8"/>
    </linearGradient>
    <linearGradient id="g-nav" x1="0" y1="0" x2="1" y2="0">
      <stop offset="0" stop-color="#34c26a"/><stop offset=".5" stop-color="#2692b8"/><stop offset="1" stop-color="#0f46d6"/>
    </linearGradient>
    <linearGradient id="g-heart" x1="0" y1="0" x2="1" y2="1">
      <stop offset="0" stop-color="#34c26a"/><stop offset="1" stop-color="#1a5ce0"/>
    </linearGradient>
    <symbol id="i-status" viewBox="0 0 42 10">
      <rect x="0" y="6" width="2" height="3" fill="#fff"/><rect x="3" y="4.5" width="2" height="4.5" fill="#fff"/><rect x="6" y="3" width="2" height="6" fill="#fff"/><rect x="9" y="1.5" width="2" height="7.5" fill="#fff"/>
      <path d="M15 4a6 6 0 0 1 8 0l-1 1a4.5 4.5 0 0 0-6 0zM17 6a3 3 0 0 1 4 0l-2 2z" fill="#fff"/>
      <rect x="27" y="1.5" width="13" height="7" rx="2" fill="#fff"/>
    </symbol>
    <symbol id="i-broken" viewBox="0 0 24 24">
      <path d="M12 21 3.5 12.6A5 5 0 0 1 11 6l1 1-1.5 4 3 2-1.5 3 2.5-3-3-2 1.5-3.5A5 5 0 0 1 20.5 12.6Z" fill="#2d3e6b"/>
    </symbol>
    <symbol id="i-x" viewBox="0 0 24 24">
      <path d="M5 5 19 19M19 5 5 19" stroke="#e8307a" stroke-width="2.6" stroke-linecap="round"/>
    </symbol>
    <symbol id="i-heart" viewBox="0 0 24 24">
      <path d="M12 21 3.5 12.6A5 5 0 0 1 12 6.3a5 5 0 0 1 8.5 6.3Z" fill="url(#g-heart)"/>
    </symbol>
    <symbol id="i-star" viewBox="0 0 24 24">
      <path d="m12 3 2.7 5.6 6.1.8-4.5 4.2 1.1 6.1L12 16.8 6.6 19.7l1.1-6.1L3.2 9.4l6.1-.8Z" fill="#1a5ce0"/>
    </symbol>
    <symbol id="i-home" viewBox="0 0 24 24">
      <path d="M3 11 12 3l9 8v10h-6v-6H9v6H3Z" fill="#fff" opacity=".9"/>
    </symbol>
    <symbol id="i-search" viewBox="0 0 24 24">
      <circle cx="11" cy="11" r="6.5" fill="none" stroke="#fff" stroke-width="3"/><path d="m16 16 5 5" stroke="#fff" stroke-width="3" stroke-linecap="round"/>
    </symbol>
    <symbol id="i-chat" viewBox="0 0 24 24">
      <path d="M4 4h16a1 1 0 0 1 1 1v11a1 1 0 0 1-1 1H9l-5 4V5a1 1 0 0 1 1-1Z" fill="#fff" opacity=".8"/>
      <circle cx="8.5" cy="10.5" r="1.2" fill="#2692b8"/><circle cx="12" cy="10.5" r="1.2" fill="#2692b8"/><circle cx="15.5" cy="10.5" r="1.2" fill="#2692b8"/>
    </symbol>
    <symbol id="i-gear" viewBox="0 0 24 24">
      <path d="M10 2h4l.6 2.8 2.4 1.4 2.7-.9 2 3.4-2.1 1.9v2.8l2.1 1.9-2 3.4-2.7-.9-2.4 1.4L14 22h-4l-.6-2.8-2.4-1.4-2.7.9-2-3.4 2.1-1.9v-2.8L2.3 8.7l2-3.4 2.7.9 2.4-1.4Z" fill="#fff" opacity=".85"/>
      <circle cx="12" cy="12" r="3.2" fill="#1a5ce0"/>
    </symbol>
    <symbol id="i-mail" viewBox="0 0 24 24"><rect x="2" y="5" width="20" height="14" rx="2" fill="#4a8fe8"/><path d="m3 6 9 7 9-7" stroke="#fff" stroke-width="1.6" fill="none"/></symbol>
    <symbol id="i-lock" viewBox="0 0 24 24"><rect x="4" y="10" width="16" height="12" rx="2" fill="#1a5ce0"/><path d="M8 10V7a4 4 0 0 1 8 0v3" stroke="#1a5ce0" stroke-width="2.4" fill="none"/></symbol>
    <symbol id="i-cake" viewBox="0 0 24 24"><rect x="3" y="12" width="18" height="9" rx="1" fill="#14161c"/><rect x="11" y="5" width="2" height="6" fill="#14161c"/><circle cx="12" cy="3.5" r="1.5" fill="#14161c"/></symbol>
    <symbol id="i-female" viewBox="0 0 24 24"><circle cx="12" cy="8" r="5.5" fill="none" stroke="#14161c" stroke-width="2.4"/><path d="M12 13.5V23M8 19h8" stroke="#14161c" stroke-width="2.4"/></symbol>
    <symbol id="i-pin" viewBox="0 0 24 24"><path d="M12 22s7-7.5 7-13a7 7 0 0 0-14 0c0 5.5 7 13 7 13Z" fill="#8a8f98"/><circle cx="12" cy="9" r="2.5" fill="#fff"/></symbol>
  </defs>
</svg>

<main class="board">

  <!-- brand + style tags -->
  <div class="brand" style="left:135px;top:81px">
    <span class="brand-name">CORVELLE</span>
    <span class="brand-dot"></span>
  </div>

  <div class="tag" style="left:75px;top:242px">App design</div>
  <div class="tag" style="left:221px;top:242px">Flat style</div>
  <div class="tag" style="left:75px;top:311px">Modern</div>
  <div class="tag" style="left:193px;top:311px">Clean UI</div>
  <div class="tag" style="left:75px;top:380px">Rounded corners</div>
  <div class="tag" style="left:75px;top:449px">Playful</div>

  <!-- hero: splash -->
  <section class="screen hero" style="left:520px;top:100px;height:594px;transform:scale(.98)">
    <div class="lagoon" role="img" aria-label="Aerial photo of a turquoise tropical lagoon with a cloud heart in the sky"></div>
    <div class="status"><span>9:41</span><svg><use href="#i-status"/></svg></div>
    <div class="wordmark" style="top:192px;font-size:30px">CORVELLE</div>
    <div class="btn btn-outline" style="left:22px;top:504px;width:120px">Sign Up</div>
    <div class="btn btn-solid" style="left:142px;top:504px;width:106px">Sign in</div>
    <div class="home-bar light" style="top:572px"></div>
  </section>

  <!-- hero: discover -->
  <section class="screen hero" style="left:820px;top:100px;height:594px;transform:scale(.98)">
    <div class="status"><span>9:41</span><svg><use href="#i-status"/></svg></div>
    <svg class="hdr" viewBox="0 0 270 95" height="95" preserveAspectRatio="none"><path d="M0 0H270V62Q135 112 0 62Z" fill="url(#g-header)"/></svg>
    <div class="wordmark" style="top:40px;font-size:20px">CORVELLE</div>
    <div class="disc-title" style="top:106px">Discover</div>
    <div class="greet" style="top:138px">Dear Dorian,</div>
    <p class="copy" style="top:156px">Allow me to introduce you to <span class="name">Marisol</span>, a captivating woman who possesses an enchanting blend of qualities that perfectly align with what you seek in a partner. Her shared interest in creativity is just the beginning of the profound connection you could share. Marisol's passion for games, documentaries, music, and writing mirrors your own, promising endless hours of intellectual stimulation and shared experiences.</p>
    <div class="photo" style="left:14px;top:296px;width:242px;height:260px" role="img" aria-label="Profile photo of Marisol in a sequinned navy outfit"></div>
    <div class="actions" style="top:464px">
      <div class="act sm"><svg><use href="#i-broken"/></svg></div>
      <div class="act lg"><svg><use href="#i-x"/></svg></div>
      <div class="act lg"><svg><use href="#i-heart"/></svg></div>
      <div class="act sm"><svg><use href="#i-star"/></svg></div>
    </div>
    <svg class="nav" style="top:505px" viewBox="0 0 270 84" height="84" preserveAspectRatio="none"><path d="M0 8Q140 30 270 4V84H0Z" fill="url(#g-nav)"/></svg>
    <div class="nav-icons" style="top:540px">
      <svg><use href="#i-home"/></svg><svg><use href="#i-search"/></svg><svg><use href="#i-chat"/></svg><svg><use href="#i-gear"/></svg>
    </div>
    <div class="home-bar light" style="top:573px"></div>
  </section>

  <!-- labels -->
  <div class="label" style="left:46px;top:1127px">SPLASH SCREEN</div>
  <div class="label" style="left:413px;top:1117px">SIGN IN SCREEN</div>
  <div class="label" style="left:46px;top:1760px">DISCOVER SCREEN</div>
  <div class="label" style="left:413px;top:1510px">DISCOVER SCREEN - SCROLL DOWN</div>
  <div class="label" style="left:780px;top:2065px">DISCOVER SCREEN - FULL</div>

  <!-- splash screen -->
  <section class="screen" style="left:78px;top:803px;height:594px">
    <div class="lagoon" role="img" aria-label="Aerial photo of a turquoise tropical lagoon with a cloud heart in the sky"></div>
    <div class="status"><span>9:41</span><svg><use href="#i-status"/></svg></div>
    <div class="wordmark" style="top:192px;font-size:30px">CORVELLE</div>
    <div class="btn btn-outline" style="left:22px;top:504px;width:120px">Sign Up</div>
    <div class="btn btn-solid" style="left:142px;top:504px;width:106px">Sign in</div>
    <div class="home-bar light" style="top:572px"></div>
  </section>

  <!-- sign in screen -->
  <section class="screen" style="left:445px;top:803px;height:594px">
    <div class="lagoon" role="img" aria-label="Lagoon sky with a cloud heart" style="bottom:auto;height:200px"></div>
    <div class="status"><span>9:41</span><svg><use href="#i-status"/></svg></div>
    <div class="signin-card">
      <div class="wordmark" style="top:36px;font-size:22px;color:var(--teal)">CORVELLE</div>
      <div class="signin-title">Sign in</div>
      <div class="field" style="top:152px"><svg><use href="#i-mail"/></svg>email address</div>
      <div class="field" style="top:195px"><svg><use href="#i-lock"/></svg>password</div>
      <div class="forgot">Forgot password?</div>
      <div class="login">Log in</div>
      <div class="signup-line">Don't have an account?<b>SIGN UP</b></div>
    </div>
    <div class="home-bar" style="top:572px"></div>
  </section>

  <!-- discover screen -->
  <section class="screen" style="left:78px;top:1475px;height:594px">
    <div class="status"><span>9:41</span><svg><use href="#i-status"/></svg></div>
    <svg class="hdr" viewBox="0 0 270 95" height="95" preserveAspectRatio="none"><path d="M0 0H270V62Q135 112 0 62Z" fill="url(#g-header)"/></svg>
    <div class="wordmark" style="top:40px;font-size:20px">CORVELLE</div>
    <div class="disc-title" style="top:106px">Discover</div>
    <div class="greet" style="top:138px">Dear Dorian,</div>
    <p class="copy" style="top:156px">Allow me to introduce you to <span class="name">Marisol</span>, a captivating woman who possesses an enchanting blend of qualities that perfectly align with what you seek in a partner. Her shared interest in creativity is just the beginning of the profound connection you could share. Marisol's passion for games, documentaries, music, and writing mirrors your own, promising endless hours of intellectual stimulation and shared experiences.</p>
    <div class="photo" style="left:14px;top:296px;width:242px;height:260px" role="img" aria-label="Profile photo of Marisol in a sequinned navy outfit"></div>
    <div class="actions" style="top:464px">
      <div class="act sm"><svg><use href="#i-broken"/></svg></div>
      <div class="act lg"><svg><use href="#i-x"/></svg></div>
      <div class="act lg"><svg><use href="#i-heart"/></svg></div>
      <div class="act sm"><svg><use href="#i-star"/></svg></div>
    </div>
    <svg class="nav" style="top:505px" viewBox="0 0 270 84" height="84" preserveAspectRatio="none"><path d="M0 8Q140 30 270 4V84H0Z" fill="url(#g-nav)"/></svg>
    <div class="nav-icons" style="top:540px">
      <svg><use href="#i-home"/></svg><svg><use href="#i-search"/></svg><svg><use href="#i-chat"/></svg><svg><use href="#i-gear"/></svg>
    </div>
    <div class="home-bar light" style="top:573px"></div>
  </section>

  <!-- discover scroll down -->
  <section class="screen" style="left:445px;top:1475px;height:594px">
    <div class="status"><span>9:41</span><svg><use href="#i-status"/></svg></div>
    <svg class="hdr" viewBox="0 0 270 70" height="70" preserveAspectRatio="none"><path d="M0 0H270V38Q135 80 0 38Z" fill="url(#g-header)"/></svg>
    <div class="thread-name">Marisol</div>
    <div class="avatar abs" style="left:115px;top:47px;width:40px;height:40px;z-index:4;border:2px solid #fff" role="img" aria-label="Marisol avatar"></div>
    <p class="copy" style="top:62px">Wishing you the best on this exciting journey of love and companionship.</p>
    <div class="greet" style="top:112px">Warm regards,</div>
    <div class="sign" style="top:132px"><div class="avatar" style="width:20px;height:20px" role="img" aria-label="Anselm avatar"></div>Anselm</div>
    <div class="more" style="top:172px">
      <h4>More about Marisol</h4>
      <div class="facts">
        <div class="fact"><small>BIRTHDAY</small><span><svg><use href="#i-cake"/></svg>13 Dec, 1989</span></div>
        <div class="fact"><small>GENDER</small><span><svg><use href="#i-female"/></svg>Female</span></div>
      </div>
      <div class="row"><small>CHILDREN</small><span>No child</span></div>
      <div class="row"><small>FAMILY GOALS</small><span>Open to children</span></div>
      <div class="row"><small>DIET</small><span>Omnivore</span></div>
      <div class="row"><small>DRINKING</small><span>Occasionally</span></div>
      <div class="row"><small>DRUGS</small><span>No</span></div>
    </div>
    <div class="actions" style="top:464px">
      <div class="act sm"><svg><use href="#i-broken"/></svg></div>
      <div class="act lg"><svg><use href="#i-x"/></svg></div>
      <div class="act lg"><svg><use href="#i-heart"/></svg></div>
      <div class="act sm"><svg><use href="#i-star"/></svg></div>
    </div>
    <svg class="nav" style="top:505px" viewBox="0 0 270 84" height="84" preserveAspectRatio="none"><path d="M0 8Q140 30 270 4V84H0Z" fill="url(#g-nav)"/></svg>
    <div class="nav-icons" style="top:540px">
      <svg><use href="#i-home"/></svg><svg><use href="#i-search"/></svg><svg><use href="#i-chat"/></svg><svg><use href="#i-gear"/></svg>
    </div>
    <div class="home-bar light" style="top:573px"></div>
  </section>

  <!-- discover full -->
  <section class="screen" style="left:812px;top:803px;height:1707px">
    <div class="status"><span>9:41</span><svg><use href="#i-status"/></svg></div>
    <svg class="hdr" viewBox="0 0 270 95" height="95" preserveAspectRatio="none"><path d="M0 0H270V62Q135 112 0 62Z" fill="url(#g-header)"/></svg>
    <div class="wordmark" style="top:40px;font-size:20px">CORVELLE</div>
    <div class="disc-title" style="top:104px">Discover</div>
    <div class="greet" style="top:136px">Dear Dorian,</div>
    <p class="copy" style="top:154px">Allow me to introduce you to <span class="name">Marisol</span>, a captivating woman who possesses an enchanting blend of qualities that perfectly align with what you seek in a partner. Her shared interest in creativity is just the beginning of the profound connection you could share. Marisol's passion for games, documentaries, music, and writing mirrors your own, promising endless hours of intellectual stimulation and shared experiences.</p>
    <div class="photo" style="left:14px;top:296px;width:242px;height:286px;border-radius:12px 12px 0 0" role="img" aria-label="Profile photo of Marisol in a sequinned navy outfit"></div>
    <div class="prof-card" style="top:582px;border-radius:0 0 10px 10px">
      <div class="prof-name">Marisol <span style="font-weight:400">34</span><i></i></div>
      <div class="prof-role"><span>Singer/Songwriter</span><span style="display:flex;align-items:center;gap:3px;font-size:7px"><svg width="8" height="8"><use href="#i-pin"/></svg>1 km away</span></div>
      <div class="chips">
        <span class="chip">Music</span><span class="chip">Singing</span><span class="chip">Painting</span><span class="chip">Camping</span>
        <span class="chip">Adventure</span><span class="chip">Cooking</span>
      </div>
    </div>
    <p class="copy" style="top:714px">But it is her adventurous spirit and independent nature that truly sets Marisol apart. She embraces life with a discerning eye, always seeking new and exciting opportunities. Her love for the beach, fashion, walking, books, swimming, and dancing reveals a zest for life that perfectly complements your own desire for exploration and discovery.</p>
    <div class="photo beach" style="left:14px;top:840px;width:116px;height:115px;border-radius:6px" role="img" aria-label="Marisol lying on a sandy beach"></div>
    <div class="photo sky" style="left:140px;top:840px;width:116px;height:115px;border-radius:6px" role="img" aria-label="Marisol standing by the sea in a white top"></div>
    <p class="copy" style="top:973px">Beyond her shared interests, Marisol's self-identification as creative, independent, and discerning resonates deeply with your own values. Her vibrant personality and unwavering sense of self make her an intriguing and captivating individual, one who possesses the potential to ignite a passionate and fulfilling romance.</p>
    <p class="copy" style="top:1085px">In Marisol, you may find a kindred spirit, a partner who not only shares your interests but also complements your desires for adventure and creativity. I encourage you to explore the possibilities that lie within this promising connection.</p>
    <p class="copy" style="top:1181px">Wishing you the best on this exciting journey of love and companionship.</p>
    <div class="greet" style="top:1230px">Warm regards,</div>
    <div class="sign" style="top:1250px"><div class="avatar" style="width:20px;height:20px" role="img" aria-label="Anselm avatar"></div>Anselm</div>
    <div class="more" style="top:1289px">
      <h4>More about Marisol</h4>
      <div class="facts">
        <div class="fact"><small>BIRTHDAY</small><span><svg><use href="#i-cake"/></svg>13 Dec, 1989</span></div>
        <div class="fact"><small>GENDER</small><span><svg><use href="#i-female"/></svg>Female</span></div>
      </div>
      <div class="row"><small>CHILDREN</small><span>No child</span></div>
      <div class="row"><small>FAMILY GOALS</small><span>Open to children</span></div>
      <div class="row"><small>DIET</small><span>Omnivore</span></div>
      <div class="row"><small>DRINKING</small><span>Occasionally</span></div>
      <div class="row"><small>DRUGS</small><span>No</span></div>
    </div>
    <div class="actions" style="top:1575px">
      <div class="act sm"><svg><use href="#i-broken"/></svg></div>
      <div class="act lg"><svg><use href="#i-x"/></svg></div>
      <div class="act lg"><svg><use href="#i-heart"/></svg></div>
      <div class="act sm"><svg><use href="#i-star"/></svg></div>
    </div>
    <svg class="nav" style="top:1614px" viewBox="0 0 270 84" height="84" preserveAspectRatio="none"><path d="M0 8Q140 30 270 4V84H0Z" fill="url(#g-nav)"/></svg>
    <div class="nav-icons" style="top:1650px">
      <svg><use href="#i-home"/></svg><svg><use href="#i-search"/></svg><svg><use href="#i-chat"/></svg><svg><use href="#i-gear"/></svg>
    </div>
    <div class="home-bar light" style="top:1684px"></div>
  </section>

</main>
</body>
</html>
```